VOLMA Presentation (Crescent Studies & Learning Academy)

We need a befitting corporate presentation for an international institute affiliated to a multilateral development bank based in Jeddah, Saudi Arabia. The institute primarily provides research, capacity development, knowledge-based solutions, and publications in Islamic Economics, Banking & Finance. Our services target mainly banking and financial institutions, regulatory authorities, other multi-laterals, academic institutions, and other institutions and personnel involved with development activities. The corporate presentation should reflect our vision and rich historical past. We have attached here a draft of the presentation. We need it beautifully re-designed with lots of graphics and animations. If any additional information is required, please contact us.
Updates

Please note that final project must be provided to us in PowerPoint Presentation format. Thank you.

Colors

Designer to choose colors to be used in the design.

Requirements
Must have
• Final project must be submitted to us in PowerPoint Presentation (.ppt) format.
Nice to have
• Suitable clip art images in slides containing lists or itemized content.

```html
<!DOCTYPE html>
<html lang="en">
<head>
<meta charset="utf-8">
<title>VOLMA Presentation — Crescent Studies & Learning Academy</title>
<link href="https://fonts.googleapis.com/css2?family=Roboto:wght@400;500;700;900&display=swap" rel="stylesheet">
<style>
:root{
  --bg:#e6e6e6;
  --dk:#0f4a2a;
  --gr:#1f7a3e;
  --lg:#2ea44f;
  --ol:#9ba63a;
  --tx:#333;
  --mut:#555;
}
*{box-sizing:border-box;margin:0;padding:0}
html,body{width:1200px;height:2545px;overflow:hidden;background:var(--bg);font-family:"Roboto",Arial,sans-serif;color:var(--tx)}
.slide{position:absolute;width:384px;height:216px;background:#fff;overflow:hidden;box-shadow:0 1px 3px rgba(0,0,0,.25)}
.c1{left:22px}.c2{left:417px}.c3{left:812px}
.abs{position:absolute}
.pn{position:absolute;right:6px;bottom:5px;width:11px;height:11px;border-radius:50%;background:var(--lg);color:#fff;font-size:6px;text-align:center;line-height:11px}
.mk{position:absolute;left:8px;bottom:4px;width:11px;height:11px;border-radius:50%;border:2px solid var(--gr)}
.foot{position:absolute;bottom:4px;width:100%;text-align:center;font-size:5px;color:#999;letter-spacing:.3px}
.title{position:absolute;width:100%;text-align:center;font-weight:700;color:var(--dk);font-size:17px;letter-spacing:.3px}
.photo{position:absolute}
.band{position:absolute;background:rgba(31,140,62,.9);color:#fff;font-weight:700;font-size:21px;line-height:1.15;padding:8px 12px}
.brand{font-weight:700;color:var(--gr);font-size:14px;display:flex;align-items:center;gap:5px}
.brand i{display:inline-block;width:12px;height:12px;border-radius:50%;background:var(--gr)}
.sm{font-size:6px;line-height:1.3;color:var(--mut)}
.pill{position:absolute;background:#fff;border-radius:12px;box-shadow:0 1px 3px rgba(0,0,0,.3);font-size:6.3px;text-align:center;display:flex;align-items:center;justify-content:center;color:#222;line-height:1.1;padding:0 4px}
.bar{position:absolute;background:var(--lg);color:#fff;font-size:6.2px;line-height:1.2;padding:0 10px;display:flex;align-items:center}
.cover{position:absolute;width:38px;height:52px;box-shadow:0 1px 2px rgba(0,0,0,.3)}
.stat{text-align:center;font-size:6px;color:#444;line-height:1.3}
.stat i{display:block;width:38px;height:38px;border-radius:50%;border:4px solid #cfe6d5;margin:0 auto 4px}
.dot{display:inline-block;width:16px;height:16px;border-radius:50%;background:var(--lg);vertical-align:middle;margin-right:8px}
</style>
</head>
<body>

<!-- Row 1 -->
<section class="slide c1" style="top:22px">
  <div class="photo" role="img" aria-label="Financial market numbers background" style="inset:0;background:linear-gradient(120deg,#1f8a4a,#1b3c8c 60%,#2a6dbb)"></div>
  <div class="abs" style="left:12px;top:10px;width:360px;height:184px;background:rgba(255,255,255,.9)"></div>
  <div class="abs" style="left:0;top:55px;width:384px;text-align:center;font-weight:900;font-size:17px;line-height:1.3;color:#111">CRESCENT STUDIES &amp; LEARNING<br>ACADEMY<br><span style="font-size:13px">( VOLMA )</span></div>
  <div class="abs brand" style="left:28px;top:168px"><i></i>VOLMA</div>
  <div class="abs" style="left:112px;top:164px;font-size:8px;color:var(--dk);text-align:center;font-weight:500">Member of the<br>Meridian Development Bank Group</div>
  <div class="abs" style="left:305px;top:150px;width:46px;height:38px;border-radius:50%;background:var(--lg)"></div>
  <div class="abs" style="left:0;top:200px;width:384px;text-align:center;font-size:8px;color:#fff;font-weight:700">www.volma.org</div>
</section>

<section class="slide c2" style="top:22px">
  <div class="photo" role="img" aria-label="Green financial numbers background" style="left:190px;top:0;width:194px;height:216px;background:linear-gradient(135deg,#1f8a4a,#0f3d24)"></div>
  <svg class="abs" width="384" height="216" style="left:0;top:0"><polygon points="0,0 235,0 290,108 235,216 0,216" fill="#fff"/><polygon points="235,0 260,0 315,108 260,216 235,216 290,108" fill="#2ea44f"/></svg>
  <div class="abs brand" style="left:85px;top:28px"><i></i>VOLMA</div>
  <div class="abs" style="left:10px;top:64px;width:210px;text-align:center;font-weight:900;font-size:13px;line-height:1.3;color:#111">CRESCENT STUDIES &amp; LEARNING<br>ACADEMY<br><span style="font-size:8px;font-weight:500">( VOLMA )</span></div>
  <div class="abs sm" style="left:10px;top:192px;font-size:5px">Member of the Meridian<br>Development Bank Group</div>
  <div class="abs" style="left:84px;top:188px;width:20px;height:18px;border-radius:50%;background:var(--lg)"></div>
  <div class="abs" style="left:312px;top:204px;font-size:8px;color:#fff">www.volma.org</div>
</section>

<section class="slide c3" style="top:22px">
  <div class="photo" role="img" aria-label="Dark green financial data background" style="inset:0;background:linear-gradient(120deg,#0b2a1c,#1e6a3a)"></div>
  <svg class="abs" width="384" height="216" style="left:0;top:0"><path d="M150,0 C110,70 120,160 200,216 L384,216 L384,0 Z" fill="#fff"/><path d="M150,0 C110,70 120,160 200,216" stroke="#2ea44f" stroke-width="6" fill="none"/><path d="M130,0 C80,80 95,170 160,216" stroke="#0f3d24" stroke-width="10" fill="none"/></svg>
  <div class="abs brand" style="left:228px;top:20px;font-size:12px"><i></i>VOLMA</div>
  <div class="abs" style="left:130px;top:80px;width:254px;text-align:center;font-weight:700;font-size:12px;line-height:1.25;color:var(--gr)">CRESCENT STUDIES &amp; LEARNING<br>ACADEMY<br><span style="font-size:7px">( VOLMA )</span></div>
  <div class="abs" style="left:4px;top:198px;font-size:11px;color:#fff;font-weight:700">www.volma.org</div>
  <div class="abs" style="left:292px;top:176px;width:22px;height:16px;border-radius:50%;background:var(--lg)"></div>
  <div class="abs sm" style="left:255px;top:196px;width:90px;font-size:5px;text-align:center">Member of the<br>Meridian Development Bank Group</div>
</section>

<!-- Row 2 -->
<section class="slide c1" style="top:253px">
  <div class="title" style="top:10px;font-size:20px">MDB GROUP</div>
  <svg class="abs" width="384" height="216" style="left:0;top:0">
    <g transform="translate(192,150)">
      <path d="M-95,0 A95,95 0 0 1 -78,-54 L-41,-28 A50,50 0 0 0 -50,0Z" fill="#223a8a"/>
      <path d="M-74,-60 A95,95 0 0 1 -25,-92 L-13,-48 A50,50 0 0 0 -39,-31Z" fill="#0f4a2a"/>
      <path d="M-18,-93 A95,95 0 0 1 36,-88 L19,-46 A50,50 0 0 0 -10,-49Z" fill="#1a5c8a"/>
      <path d="M42,-85 A95,95 0 0 1 84,-44 L44,-23 A50,50 0 0 0 22,-45Z" fill="#2ea44f"/>
      <path d="M87,-38 A95,95 0 0 1 95,10 L50,5 A50,50 0 0 0 46,-20Z" fill="#9ba63a"/>
    </g>
    <g font-size="7" fill="#fff" font-family="Roboto" font-weight="700" text-anchor="middle">
      <text x="125" y="131">1981</text><text x="152" y="93">1994</text><text x="199" y="82">1999</text><text x="242" y="103">2005</text><text x="263" y="142">2008</text>
    </g>
  </svg>
  <div class="abs" style="left:152px;top:128px;width:80px;text-align:center;font-weight:700;color:#1a3f8a;font-size:14px">MDB<div style="font-size:5px;color:#555;font-weight:400">Meridian Development Bank</div></div>
  <div class="abs sm" style="left:20px;top:62px;width:80px;text-align:center;font-size:5px"><b style="font-size:10px;color:var(--ol)">MECC</b><br>Meridian Export Credit Corp.</div>
  <div class="abs sm" style="left:130px;top:38px;width:90px;text-align:center;font-size:5px">Meridian Private Sector Corp. <b style="color:#1a5c8a;font-size:8px">MPSC</b></div>
  <div class="abs sm" style="left:275px;top:68px;width:70px;text-align:center;font-size:5px">Meridian Solidarity Fund</div>
  <div class="abs sm" style="left:18px;top:150px;width:72px;text-align:center;font-size:5px"><b style="color:var(--gr);font-size:9px">VOLMA</b><br>Crescent Studies &amp; Learning Academy</div>
  <div class="abs sm" style="left:296px;top:150px;width:80px;text-align:center;font-size:5px"><b style="color:#c0392b;font-size:9px">MTFC</b><br>Meridian Trade Finance Corp.</div>
  <div class="mk"></div><div class="pn">4</div>
</section>

<section class="slide c2" style="top:253px">
  <div class="photo" role="img" aria-label="Stacks of coins" style="left:110px;top:0;width:274px;height:216px;background:linear-gradient(90deg,#fff,#9b8a5a 40%,#4a3d22)"></div>
  <div class="abs brand" style="left:30px;top:60px;font-size:22px"><i style="width:20px;height:20px"></i>VOLMA</div>
  <div class="abs sm" style="left:28px;top:95px;font-size:5px;color:var(--gr)">CRESCENT STUDIES &amp; LEARNING ACADEMY<br>A member of the Meridian Development Bank Group</div>
  <div class="band" style="left:0;top:155px;width:384px;height:34px;background:var(--dk);padding:6px 22px">ABOUT VOLMA</div>
  <div class="pn">5</div>
</section>

<section class="slide c3" style="top:253px">
  <div class="title" style="top:14px;color:#222;font-size:20px">ABOUT VOLMA</div>
  <div class="bar" style="left:26px;top:56px;width:324px;height:24px">We provide innovative, knowledge-based solutions for development challenges faced by MDB member countries in accordance with sound principles.</div>
  <div class="bar" style="left:26px;top:90px;width:324px;height:24px;background:var(--dk)">We conduct cutting-edge research programs in Islamic Economics and Finance to achieve the SDGs.</div>
  <div class="bar" style="left:26px;top:124px;width:324px;height:28px">The Academy is responsible for knowledge creation and dissemination in Islamic Economics and Finance for member countries.</div>
  <div class="bar" style="left:26px;top:162px;width:324px;height:20px;background:var(--dk)">We provide learning and capacity building programs for MDB member countries.</div>
  <svg class="abs" width="30" height="140" style="left:345px;top:54px" fill="#fff" stroke="#1f7a3e" stroke-width="2"><circle cx="15" cy="14" r="11"/><circle cx="15" cy="48" r="11"/><circle cx="15" cy="84" r="11"/><circle cx="15" cy="118" r="11"/></svg>
  <div class="mk"></div><div class="pn">6</div>
</section>

<!-- Row 3 -->
<section class="slide c1" style="top:484px">
  <div class="title" style="top:30px">VOLMA MILESTONES</div>
  <div class="abs" style="left:0;top:122px;width:384px;height:10px;background:var(--dk);display:flex;justify-content:space-around;color:#fff;font-size:6px;font-weight:700;align-items:center">
    <span>1981</span><span>1983</span><span>1988</span><span>2003</span><span>2005</span><span>2008</span><span>2009</span><span>2010</span><span>2011</span><span>2013</span><span>2015</span><span>2019</span><span>2019</span>
  </div>
  <div class="abs" style="left:14px;top:72px;width:356px;display:flex;justify-content:space-around;align-items:flex-end;height:45px;font-size:4.5px;color:#444;text-align:center">
    <span style="width:28px">Operational</span><span style="width:28px">Became MDB group entity</span><span style="width:28px">Launched solidarity prize and trade programs</span><span style="width:28px">Launched global leadership program</span><span style="width:28px">Initiated flagship country reports</span><span style="width:28px">Approved smart economy lab</span>
  </div>
  <div class="abs" style="left:0;top:140px;width:384px;display:flex;justify-content:space-around;font-size:4.5px;color:#444;text-align:center">
    <span style="width:26px">Established</span><span style="width:26px">Launched first prize</span><span style="width:26px">Launched distance learning program</span><span style="width:26px">Launched scholarships &amp; research grants</span><span style="width:26px">Launched e-learning masters</span><span style="width:26px">Moved programs online</span><span style="width:26px">Filed patents for two solutions</span>
  </div>
  <div class="mk"></div><div class="pn">7</div>
</section>

<section class="slide c2" style="top:484px">
  <div class="abs" style="left:16px;top:16px;font-weight:700;font-size:17px;color:var(--dk);line-height:1.2;text-align:center">VOLMA<br>IN NUMBERS</div>
  <div class="photo" role="img" aria-label="Silhouettes of two business people" style="left:36px;top:70px;width:90px;height:115px;background:linear-gradient(90deg,#1f7a3e 50%,#aaa 50%);border-radius:30px 30px 0 0"></div>
  <div class="abs" style="left:178px;top:14px;width:190px;font-size:5.5px;color:#333">
    <div style="position:relative;height:21px"><span class="abs" style="left:8px">Shariah Specialists</span><b class="abs" style="left:-6px;top:4px">3</b><div class="abs" style="left:5px;top:8px;width:170px;height:5px;border:1px solid var(--lg);border-radius:3px"><div style="width:20%;height:100%;background:var(--lg)"></div></div></div>
    <div style="position:relative;height:21px"><span class="abs" style="left:8px">Publications Specialists</span><b class="abs" style="left:-6px;top:4px">5</b><div class="abs" style="left:5px;top:8px;width:170px;height:5px;border:1px solid var(--lg);border-radius:3px"><div style="width:35%;height:100%;background:var(--lg)"></div></div></div>
    <div style="position:relative;height:21px"><span class="abs" style="left:8px">Researchers</span><b class="abs" style="left:-6px;top:4px">9</b><div class="abs" style="left:5px;top:8px;width:170px;height:5px;border:1px solid var(--lg);border-radius:3px"><div style="width:85%;height:100%;background:var(--lg)"></div></div></div>
    <div style="position:relative;height:21px"><span class="abs" style="left:8px">Technology Specialists</span><b class="abs" style="left:-6px;top:4px">2</b><div class="abs" style="left:5px;top:8px;width:170px;height:5px;border:1px solid var(--lg);border-radius:3px"><div style="width:15%;height:100%;background:var(--lg)"></div></div></div>
    <div style="position:relative;height:21px"><span class="abs" style="left:8px">Management</span><b class="abs" style="left:-6px;top:4px">5</b><div class="abs" style="left:5px;top:8px;width:170px;height:5px;border:1px solid var(--lg);border-radius:3px"><div style="width:35%;height:100%;background:var(--lg)"></div></div></div>
    <div style="position:relative;height:21px"><span class="abs" style="left:8px">Training Specialists</span><b class="abs" style="left:-6px;top:4px">6</b><div class="abs" style="left:5px;top:8px;width:170px;height:5px;border:1px solid var(--lg);border-radius:3px"><div style="width:45%;height:100%;background:var(--lg)"></div></div></div>
    <div style="position:relative;height:21px"><span class="abs" style="left:8px">Administrative Specialists</span><b class="abs" style="left:-8px;top:4px">10</b><div class="abs" style="left:5px;top:8px;width:170px;height:5px;border:1px solid var(--lg);border-radius:3px"><div style="width:95%;height:100%;background:var(--lg)"></div></div></div>
    <div style="position:relative;height:21px"><span class="abs" style="left:8px">Financial Analysts</span><b class="abs" style="left:-6px;top:4px">2</b><div class="abs" style="left:5px;top:8px;width:170px;height:5px;border:1px solid var(--lg);border-radius:3px"><div style="width:15%;height:100%;background:var(--lg)"></div></div></div>
  </div>
  <div class="mk"></div><div class="pn">8</div>
</section>

<section class="slide c3" style="top:484px">
  <div class="title" style="top:16px">VOLMA IN NUMBERS (1981-2019)</div>
  <div class="abs" style="left:20px;top:50px;width:344px;display:grid;grid-template-columns:repeat(4,1fr);row-gap:10px">
    <div class="stat"><i style="background:var(--dk)"></i>377<br>RESEARCH PROJECTS</div>
    <div class="stat"><i style="background:var(--lg)"></i>405<br>CONFERENCES</div>
    <div class="stat"><i style="background:var(--dk)"></i>729<br>TRAINING PROGRAMS</div>
    <div class="stat"><i style="background:var(--lg)"></i>8<br>ONLINE LEARNING PROGRAMS</div>
    <div class="stat"><i style="background:var(--lg)"></i>19<br>ADVISORY PROJECTS</div>
    <div class="stat"><i style="background:var(--dk)"></i>63<br>ENCOURAGEMENT PROGRAMS</div>
    <div class="stat"><i style="background:var(--lg)"></i>23<br>KNOWLEDGE DISSEMINATION</div>
    <div class="stat"><i style="background:var(--dk)"></i>513<br>PUBLICATIONS</div>
  </div>
  <div class="mk"></div><div class="pn">9</div>
</section>

<!-- Row 4 -->
<section class="slide c1" style="top:714px">
  <div class="photo" role="img" aria-label="Green-tinted office building" style="inset:0;background:linear-gradient(120deg,#1e6a3a,#2f8a4e 60%,#5aa870)"></div>
  <div class="abs" style="left:14px;top:96px;color:#fff;font-weight:700;font-size:26px">WHAT WE DO</div>
  <div class="abs" style="left:60px;top:126px;color:#fff;font-weight:700;font-size:11px">VOLMA ACTIVITIES</div>
  <div class="abs" style="left:222px;top:22px;width:162px;font-size:8px;color:#fff">
    <div style="background:rgba(255,255,255,.22);padding:5px 12px;margin-bottom:23px">Capacity Development</div>
    <div style="background:rgba(255,255,255,.22);padding:5px 12px;margin-bottom:23px">Knowledge Solutions</div>
    <div style="background:rgba(255,255,255,.22);padding:5px 12px;margin-bottom:23px">Innovative Research</div>
    <div style="background:rgba(255,255,255,.22);padding:5px 12px">Publications &amp; Information Services</div>
  </div>
  <div class="pn" style="background:none">10</div>
</section>

<section class="slide c2" style="top:714px">
  <div class="photo" role="img" aria-label="Person working at a laptop" style="inset:0;background:linear-gradient(120deg,#3a4040,#1a1e1e)"></div>
  <div class="band" style="left:98px;top:72px;width:286px;height:70px">INNOVATIVE<br>RESEARCH</div>
  <div class="pn" style="background:none">11</div>
</section>

<section class="slide c3" style="top:714px">
  <div class="title" style="top:20px">INNOVATIVE RESEARCH</div>
  <div class="photo" role="img" aria-label="Magnifying glass illustration" style="left:118px;top:50px;width:150px;height:150px;background:radial-gradient(circle at 45% 42%,#f1f1f1 0,#e4e4e4 45%,rgba(255,255,255,0) 70%)"></div>
  <div class="abs" style="left:52px;top:70px;width:40px;height:22px;background:var(--dk);color:#fff;font-weight:700;font-size:12px;text-align:center;line-height:22px;border-radius:12px 0 12px 0">01</div>
  <div class="abs" style="left:172px;top:70px;width:40px;height:22px;background:var(--ol);color:#fff;font-weight:700;font-size:12px;text-align:center;line-height:22px;border-radius:12px 0 12px 0">02</div>
  <div class="abs" style="left:272px;top:70px;width:40px;height:22px;background:var(--lg);color:#fff;font-weight:700;font-size:12px;text-align:center;line-height:22px;border-radius:12px 0 12px 0">03</div>
  <div class="abs sm" style="left:24px;top:108px;width:100px;text-align:center;font-size:5.5px">We are a pioneer in conducting, promoting and encouraging research innovation and knowledge creation in Islamic Economics, Banking and Finance.</div>
  <div class="abs sm" style="left:147px;top:106px;width:90px;text-align:center;font-size:5.5px">Our research formulates solutions and strategies for addressing the challenges in accordance with the principles of Islamic Economics and Finance.</div>
  <div class="abs sm" style="left:258px;top:108px;width:100px;text-align:center;font-size:5.5px">Our research seeks to identify challenges of economic development facing MDB Member Countries.</div>
  <div class="foot">INNOVATIVE RESEARCH</div>
  <div class="mk"></div><div class="pn">12</div>
</section>

<!-- Row 5 -->
<section class="slide c1" style="top:945px">
  <div class="title" style="top:24px">RESEARCH PRODUCTS &amp; SERVICES</div>
  <div class="abs" style="left:24px;top:72px;display:flex">
    <div style="width:92px;height:92px;border-radius:50%;border:9px solid var(--dk);display:flex;align-items:center;justify-content:center;text-align:center;font-size:7px;background:#fff;position:relative;z-index:4;padding:6px">In-house and Joint Research</div>
    <div style="width:92px;height:92px;border-radius:50%;border:9px solid var(--lg);display:flex;align-items:center;justify-content:center;text-align:center;font-size:6.5px;margin-left:-10px;background:#fff;position:relative;z-index:3;padding:8px">Research products (journals, books, reports, lectures, etc.)</div>
    <div style="width:92px;height:92px;border-radius:50%;border:9px solid var(--dk);display:flex;align-items:center;justify-content:center;text-align:center;font-size:6.5px;margin-left:-10px;background:#fff;position:relative;z-index:2;padding:8px">Research Events (conferences, workshops, symposiums, etc.)</div>
    <div style="width:92px;height:92px;border-radius:50%;border:9px solid var(--lg);display:flex;align-items:center;justify-content:center;text-align:center;font-size:7px;margin-left:-10px;background:#fff;position:relative;z-index:1">MDB Prize</div>
  </div>
  <div class="foot">INNOVATIVE RESEARCH</div>
  <div class="mk"></div><div class="pn">13</div>
</section>

<section class="slide c2" style="top:945px">
  <svg class="abs" width="384" height="216" style="left:0;top:0" stroke="#2ea44f" stroke-width=".8" fill="none">
    <path d="M104,25 L150,100 M104,68 L150,100 M104,108 L150,105 M104,150 L150,110 M104,185 L150,115"/>
    <path d="M276,26 L235,100 M276,68 L235,100 M276,108 L235,105 M276,149 L235,110 M276,183 L235,115"/>
  </svg>
  <div class="pill" style="left:14px;top:14px;width:90px;height:22px">Islamic Financial Inclusion</div>
  <div class="pill" style="left:14px;top:58px;width:90px;height:20px">Islamic Banking</div>
  <div class="pill" style="left:14px;top:98px;width:90px;height:20px">Sukuk and Islamic Capital Market</div>
  <div class="pill" style="left:14px;top:136px;width:90px;height:28px">Comprehensive Human Development Based on Sharia Goals</div>
  <div class="pill" style="left:14px;top:176px;width:90px;height:18px">Shariah Structuring</div>
  <div class="abs" style="left:147px;top:55px;width:90px;height:90px;border-radius:50%;background:var(--dk);color:#fff;font-weight:700;font-size:11px;display:flex;align-items:center;justify-content:center;text-align:center">RESEARCH<br>AREAS</div>
  <div class="pill" style="left:276px;top:16px;width:90px;height:20px">Smart Economy</div>
  <div class="pill" style="left:276px;top:58px;width:90px;height:20px">Islamic Fintech</div>
  <div class="pill" style="left:276px;top:98px;width:90px;height:20px">Zakat Management</div>
  <div class="pill" style="left:276px;top:136px;width:90px;height:26px">Management and Development of Awqaf</div>
  <div class="pill" style="left:276px;top:174px;width:90px;height:18px">Islamic Microfinance</div>
  <div class="foot">INNOVATIVE RESEARCH</div>
  <div class="mk"></div><div class="pn">14</div>
</section>

<section class="slide c3" style="top:945px">
  <div class="photo" role="img" aria-label="Gears on a blue background" style="inset:0;background:linear-gradient(120deg,#1f3040,#33506a)"></div>
  <div class="band" style="left:98px;top:72px;width:286px;height:70px">CAPACITY<br>DEVELOPMENT</div>
  <div class="pn" style="background:none">15</div>
</section>

<!-- Row 6 -->
<section class="slide c1" style="top:1175px">
  <div class="title" style="top:14px">CAPACITY DEVELOPMENT</div>
  <div class="abs" style="left:0;top:42px;width:210px;height:146px;background:var(--gr)"></div>
  <div class="photo" role="img" aria-label="Business people joining hands" style="left:205px;top:42px;width:179px;height:146px;background:linear-gradient(120deg,#c9d6e0,#6d8aa0)"></div>
  <svg class="abs" width="12" height="12" style="left:14px;top:72px"><circle cx="6" cy="6" r="6" fill="#fff"/><path d="M3,6 L5.5,8.5 L9,4" stroke="#1f7a3e" stroke-width="1.5" fill="none"/></svg>
  <div class="abs" style="left:40px;top:66px;width:150px;font-size:6.5px;color:#fff;line-height:1.3">VOLMA is the largest contributor to human capital development in Islamic Economics, Banking and Finance.</div>
  <svg class="abs" width="12" height="12" style="left:14px;top:125px"><circle cx="6" cy="6" r="6" fill="#fff"/><path d="M3,6 L5.5,8.5 L9,4" stroke="#1f7a3e" stroke-width="1.5" fill="none"/></svg>
  <div class="abs" style="left:40px;top:112px;width:150px;font-size:6.5px;color:#fff;line-height:1.3">We develop human resources and technical capacity in Islamic Economics, Banking and Finance by providing training courses by both online and face to face.</div>
  <div class="mk"></div><div class="pn">16</div>
</section>

<section class="slide c2" style="top:1175px">
  <div class="title" style="top:18px">PROGRAMS</div>
  <div class="abs" style="left:70px;top:52px;font-size:6px;text-align:center">Programs for MDB<br>Member Countries</div>
  <div class="abs" style="left:188px;top:62px;font-size:6px">Training Packages</div>
  <div class="abs" style="left:280px;top:62px;font-size:6px">Online Learning Programs</div>
  <svg class="abs" role="img" aria-label="Photos of training sessions and a certificate" width="354" height="82" style="left:16px;top:74px">
    <polygon points="0,80 45,0 90,80" fill="#8a6a4a"/>
    <polygon points="50,0 140,0 95,80" fill="#b88a50"/>
    <polygon points="100,80 145,0 190,80" fill="#a05a3a"/>
    <polygon points="150,0 240,0 195,80" fill="#6a8aaa"/>
    <polygon points="200,80 245,0 290,80" fill="#9ab0c0"/>
    <polygon points="250,0 340,0 295,80" fill="#cfd8dc"/>
  </svg>
  <div class="abs" style="left:18px;top:160px;font-size:6px;text-align:center">Programs for Private<br>Sector</div>
  <div class="abs" style="left:118px;top:160px;font-size:6px;text-align:center">Knowledge Leaders<br>Programs</div>
  <div class="abs" style="left:226px;top:160px;font-size:6px">Certification Program</div>
  <div class="foot">CAPACITY DEVELOPMENT</div>
  <div class="mk"></div><div class="pn">17</div>
</section>

<section class="slide c3" style="top:1175px">
  <svg class="abs" width="384" height="216" style="left:0;top:0">
    <circle cx="192" cy="110" r="52" stroke="#1f7a3e" stroke-width="7" fill="none" stroke-dasharray="30 10"/>
    <polygon points="188,22 196,22 196,45 202,45 192,55 182,45 188,45" fill="#1f7a3e"/>
    <g stroke="#9ba63a" stroke-width="5"><line x1="228" y1="80" x2="262" y2="60"/><line x1="240" y1="115" x2="275" y2="125"/><line x1="150" y1="80" x2="122" y2="62"/></g>
    <g stroke="#2ea44f" stroke-width="5"><line x1="225" y1="150" x2="248" y2="172"/><line x1="145" y1="128" x2="110" y2="135"/><line x1="170" y1="160" x2="155" y2="180"/></g>
  </svg>
  <div class="abs" style="left:152px;top:98px;width:80px;text-align:center;font-weight:700;font-size:17px;color:#111">TOPICS</div>
  <div class="abs sm" style="left:0;top:8px;width:384px;text-align:center">Principles of Islamic Economics, Banking &amp; Finance</div>
  <div class="abs sm" style="left:10px;top:45px;width:100px;text-align:center">Corporate Governance for Islamic Financial Institutions</div>
  <div class="abs sm" style="left:268px;top:45px;width:106px">Regulation and Supervision of Islamic Banks</div>
  <div class="abs sm" style="left:282px;top:118px;width:90px">Risk Management in Islamic Financial Institutions</div>
  <div class="abs sm" style="left:4px;top:134px;width:100px;text-align:center">Shari'ah Standards for Islamic Financial Institutions</div>
  <div class="abs sm" style="left:252px;top:178px;width:120px">Shari'ah Supervision and Auditing of Islamic Financial Institutions</div>
  <div class="abs sm" style="left:48px;top:188px;width:110px">Sukuk: Shari'ah and Operational Aspects</div>
  <div class="foot">CAPACITY DEVELOPMENT</div>
  <div class="mk"></div><div class="pn">18</div>
</section>

<!-- Row 7 -->
<section class="slide c1" style="top:1398px">
  <div class="title" style="top:10px;color:#111">TOPICS</div>
  <svg class="abs" width="384" height="216" style="left:0;top:0">
    <path d="M0,118 Q24,100 49,118 T98,118 T147,118 T196,118 T245,118 T294,118 T343,118 T392,118" stroke="#1f7a3e" stroke-width="14" fill="none"/>
    <g fill="#2ea44f"><rect x="38" y="82" width="24" height="30"/><rect x="136" y="82" width="24" height="30"/><rect x="234" y="82" width="24" height="30"/><rect x="332" y="82" width="24" height="30"/></g>
    <g fill="#0f4a2a"><rect x="86" y="124" width="24" height="30"/><rect x="184" y="124" width="24" height="30"/><rect x="282" y="124" width="24" height="30"/></g>
    <g fill="#fff" font-family="Roboto" font-size="13" font-weight="700" text-anchor="middle"><text x="50" y="102">01</text><text x="148" y="102">03</text><text x="246" y="102">05</text><text x="344" y="102">07</text><text x="98" y="144">02</text><text x="196" y="144">04</text><text x="294" y="144">06</text></g>
  </svg>
  <div class="abs sm" style="left:4px;top:40px;width:80px;text-align:center;color:#222">Liquidity Management in Islamic Financial Institutions</div>
  <div class="abs sm" style="left:110px;top:40px;width:76px;text-align:center;color:#222">Management of Zakah for Poverty Alleviation</div>
  <div class="abs sm" style="left:206px;top:46px;width:80px;text-align:center;color:#222">Islamic Microfinance for Poverty Alleviation</div>
  <div class="abs sm" style="left:296px;top:40px;width:86px;text-align:center;color:#222">Public-Private Partnership (PPP) for Infrastructure Projects</div>
  <div class="abs sm" style="left:58px;top:162px;width:80px;text-align:center;color:#222">Islamic Capital Markets</div>
  <div class="abs sm" style="left:156px;top:162px;width:80px;text-align:center;color:#222">Management of Awqaf for Poverty Alleviation</div>
  <div class="abs sm" style="left:254px;top:162px;width:80px;text-align:center;color:#222">Financing Small and Medium Enterprises (SMEs)</div>
  <div class="foot">CAPACITY DEVELOPMENT</div>
  <div class="mk"></div><div class="pn">19</div>
</section>

<section class="slide c2" style="top:1398px">
  <div class="title" style="top:14px">ONLINE LEARNING PROGRAMS</div>
  <div class="abs" style="left:46px;top:46px;width:62px;height:62px;border-radius:50%;border:3px solid var(--lg);text-align:center;font-size:7px;font-weight:700;color:var(--gr);padding-top:18px">VOLMA on<br>OpenCourse</div>
  <div class="abs" style="left:20px;top:120px;width:130px;height:50px;background:#fff;box-shadow:0 1px 4px rgba(0,0,0,.3);border-radius:6px"></div>
  <svg class="abs" width="24" height="20" style="left:34px;top:136px" fill="#1f7a3e"><rect x="0" y="8" width="3" height="12"/><rect x="6" y="4" width="3" height="16"/><rect x="12" y="10" width="3" height="10"/><rect x="18" y="6" width="3" height="14"/></svg>
  <div class="abs" style="left:86px;top:124px;text-align:center;color:var(--lg);font-weight:700;font-size:13px;line-height:1">45.000<div style="font-size:6px;color:#444">Beneficiaries</div>8<div style="font-size:6px;color:#444">Courses</div></div>
  <svg class="abs" width="40" height="60" style="left:150px;top:60px" stroke="#2ea44f" stroke-dasharray="2 2" fill="none"><path d="M0,20 L38,20 M0,86 L38,86"/></svg>
  <div class="abs" role="img" aria-label="Course thumbnails" style="left:188px;top:40px;width:180px;height:150px">
    <div class="abs" style="left:0;top:0;width:54px;height:30px;background:#6a9a7a"></div><div class="abs" style="left:62px;top:0;width:54px;height:30px;background:#7aaa8a"></div><div class="abs" style="left:124px;top:0;width:54px;height:30px;background:#5a8a6a"></div>
    <div class="abs" style="left:0;top:56px;width:54px;height:30px;background:#7aaa8a"></div><div class="abs" style="left:62px;top:56px;width:54px;height:30px;background:#5a8a6a"></div><div class="abs" style="left:124px;top:56px;width:54px;height:30px;background:#6a9a7a"></div>
    <div class="abs" style="left:20px;top:110px;width:54px;height:30px;background:#5a8a6a"></div><div class="abs" style="left:90px;top:110px;width:54px;height:30px;background:#6a9a7a"></div>
  </div>
  <div class="abs" style="left:188px;top:72px;width:180px;font-size:4.5px;color:#666;display:flex;gap:8px"><span style="width:54px">Principles of Islamic insurance</span><span style="width:54px">Islamic finance and banking</span><span style="width:54px">Capital markets</span></div>
  <div class="abs" style="left:188px;top:128px;width:180px;font-size:4.5px;color:#666;display:flex;gap:8px"><span style="width:54px">Finance and banking modes</span><span style="width:54px">Insurance and investments</span><span style="width:54px">Sukuk markets</span></div>
  <div class="abs" style="left:208px;top:182px;width:160px;font-size:4.5px;color:#666;display:flex;gap:16px"><span style="width:54px">Capital markets structure</span><span style="width:54px">Islamic banking principles</span></div>
  <div class="mk"></div><div class="pn">20</div>
</section>

<section class="slide c3" style="top:1398px">
  <div class="photo" role="img" aria-label="Hand holding glowing network" style="inset:0;background:linear-gradient(120deg,#1f2a38,#2e3e50)"></div>
  <div class="band" style="left:98px;top:72px;width:286px;height:70px">KNOWLEDGE<br>SOLUTIONS</div>
  <div class="pn" style="background:none">21</div>
</section>

<!-- Row 8 -->
<section class="slide c1" style="top:1628px">
  <div class="photo" role="img" aria-label="Hands holding digital globe of icons" style="left:0;top:0;width:178px;height:216px;background:radial-gradient(circle at 50% 50%,#3a6a9a,#10203a)"></div>
  <div class="abs" style="left:20px;top:94px;color:#fff;font-weight:700;font-size:20px">OBJECTIVES</div>
  <div class="abs" style="left:198px;top:16px;width:160px;font-size:8.3px;line-height:1.75;color:#333;text-align:justify">The Knowledge Solutions initiative aims to transform critical components of the economy of MDB's Member Countries using Fintech innovations and technologies (AI, Blockchain, IoT, etc.) to bring about value-based, inclusive and sustainable growth in line with principles of Islamic economics and finance.</div>
  <div class="pn">22</div>
</section>

<section class="slide c2" style="top:1628px">
  <div class="title" style="top:22px;font-size:18px">MAIN ACTIVITIES</div>
  <div class="abs" style="left:26px;top:58px;width:322px;height:38px;background:var(--dk);color:#fff;font-size:8px;font-weight:700;text-align:center;line-height:38px">The main activities under Knowledge Solutions initiative are:</div>
  <div class="abs" style="left:26px;top:112px;width:154px;height:64px;background:#fff;box-shadow:0 1px 4px rgba(0,0,0,.3);border-radius:8px;font-size:6.5px;padding:12px 14px;line-height:1.3;border-bottom:6px solid var(--lg)">Designing and structuring of new, innovative, knowledge-based solutions for development challenges of MDB's Member Countries</div>
  <div class="abs" style="left:194px;top:112px;width:154px;height:64px;background:#fff;box-shadow:0 1px 4px rgba(0,0,0,.3);border-radius:8px;font-size:6.5px;padding:12px 14px;line-height:1.3;border-bottom:6px solid var(--lg)">Identifying new opportunities, and emerging needs, for the delivery of innovative knowledge-solutions in the Islamic Fintech space.</div>
  <div class="foot">KNOWLEDGE SOLUTIONS</div>
  <div class="mk"></div><div class="pn">23</div>
</section>

<section class="slide c3" style="top:1628px">
  <div class="abs" style="left:16px;top:90px;width:140px;font-weight:700;font-size:16px;color:var(--dk);line-height:1.2;text-align:center">PRODUCTS AND<br>SOLUTIONS</div>
  <div class="abs sm" style="left:14px;top:134px;width:146px;text-align:center;color:var(--lg)">Some examples of knowledge products and solutions are:</div>
  <div class="bar" style="left:172px;top:26px;width:196px;height:20px;font-weight:700;padding-left:24px">Crypto-token for socio-economic impact</div>
  <div class="bar" style="left:192px;top:62px;width:176px;height:20px;background:var(--dk);font-weight:700;padding-left:20px">Smart Credit Enhancement Solution</div>
  <div class="bar" style="left:192px;top:98px;width:176px;height:20px;font-weight:700;padding-left:20px">Crypto-based Smart Voucher</div>
  <div class="bar" style="left:192px;top:134px;width:176px;height:20px;background:var(--dk);font-weight:700;padding-left:20px">... to mention few ...</div>
  <div class="bar" style="left:172px;top:170px;width:196px;height:20px;font-weight:700;padding-left:24px;font-size:5.5px">Waqf and other Sharia-compliant financial instruments on blockchain</div>
  <div class="abs" style="left:158px;top:22px;width:28px;height:28px;border-radius:50%;background:#fff;border:2px solid var(--lg);text-align:center;line-height:24px;font-size:8px">1</div>
  <div class="abs" style="left:178px;top:58px;width:28px;height:28px;border-radius:50%;background:#fff;border:2px solid var(--dk);text-align:center;line-height:24px;font-size:8px">2</div>
  <div class="abs" style="left:178px;top:94px;width:28px;height:28px;border-radius:50%;background:#fff;border:2px solid var(--lg);text-align:center;line-height:24px;font-size:8px">3</div>
  <div class="abs" style="left:178px;top:130px;width:28px;height:28px;border-radius:50%;background:#fff;border:2px solid var(--dk);text-align:center;line-height:24px;font-size:8px">4</div>
  <div class="abs" style="left:158px;top:166px;width:28px;height:28px;border-radius:50%;background:#fff;border:2px solid var(--lg);text-align:center;line-height:24px;font-size:8px">5</div>
  <div class="foot">KNOWLEDGE SOLUTIONS</div>
  <div class="mk"></div><div class="pn">24</div>
</section>

<!-- Row 9 -->
<section class="slide c1" style="top:1858px">
  <div class="photo" role="img" aria-label="Library bookshelves" style="inset:0;background:repeating-linear-gradient(180deg,#3a3430 0 26px,#1e1a18 26px 30px)"></div>
  <div class="band" style="left:98px;top:72px;width:286px;height:70px;padding:12px 12px;font-size:18px">PUBLICATIONS<br>&amp; INFORMATION SERVICES</div>
  <div class="pn" style="background:none">25</div>
</section>

<section class="slide c2" style="top:1858px">
  <div class="photo" role="img" aria-label="Library bookshelves" style="inset:0;background:repeating-linear-gradient(180deg,#3a3430 0 26px,#1e1a18 26px 30px)"></div>
  <div class="abs" style="left:0;top:55px;width:384px;height:140px;background:rgba(31,140,62,.85)"></div>
  <div class="abs" style="left:0;top:62px;width:384px;text-align:center;color:#fff;font-weight:700;font-size:15px">PUBLICATIONS &amp; INFORMATION SERVICES</div>
  <div class="abs" style="left:16px;top:98px;width:108px;height:88px;background:#fff;font-size:6.5px;text-align:center;padding:14px 8px;line-height:1.25">We have produced publications in many languages, including Arabic, English, French, Turkish, Russian, Portuguese and Bahasa Indonesia languages</div>
  <div class="abs" style="left:138px;top:98px;width:108px;height:88px;background:#fff;font-size:6.5px;text-align:center;padding:28px 8px;line-height:1.25">We lead in providing Islamic Economics, Banking and Finance publications.</div>
  <div class="abs" style="left:260px;top:98px;width:108px;height:88px;background:#fff;font-size:6.5px;text-align:center;padding:14px 8px;line-height:1.25">We produce a wide range of publications including flagship reports, textbooks, journals, conference proceedings and other research publications.</div>
  <svg class="abs" width="14" height="14" style="left:124px;top:136px"><circle cx="7" cy="7" r="7" fill="#1f7a3e"/><path d="M5.5,4 L9,7 L5.5,10" stroke="#fff" stroke-width="1.4" fill="none"/></svg>
  <svg class="abs" width="14" height="14" style="left:246px;top:136px"><circle cx="7" cy="7" r="7" fill="#1f7a3e"/><path d="M5.5,4 L9,7 L5.5,10" stroke="#fff" stroke-width="1.4" fill="none"/></svg>
  <div class="pn">26</div>
</section>

<section class="slide c3" style="top:1858px">
  <div class="photo" role="img" aria-label="Open newspapers" style="left:0;top:0;width:170px;height:216px;background:linear-gradient(120deg,#4a5258,#9aa2a8)"></div>
  <div class="abs" style="left:0;top:92px;width:170px;color:#fff;font-weight:700;font-size:16px;line-height:1.2;text-align:center">PUBLICATIONS<br>SERVICES</div>
  <svg class="abs" width="150" height="170" style="left:200px;top:22px" font-family="Roboto" font-size="6" fill="#fff" text-anchor="middle">
    <polygon points="75,85 40,24 110,24" fill="#2ea44f"/><text x="75" y="34">Books</text>
    <polygon points="75,85 110,24 145,85" fill="#0f4a2a"/><text x="122" y="78">Journals</text>
    <polygon points="75,85 145,85 110,146" fill="#9ba63a"/><text x="122" y="100">Reports</text>
    <polygon points="75,85 110,146 40,146" fill="#2ea44f"/><text x="75" y="140">Online material</text>
    <polygon points="75,85 40,146 5,85" fill="#0f4a2a"/><text x="28" y="100">Pamphlets</text>
    <polygon points="75,85 5,85 40,24" fill="#9ba63a"/><text x="28" y="78">eBooks</text>
  </svg>
  <div class="abs" style="left:170px;bottom:4px;width:214px;text-align:center;font-size:5px;color:#999">PUBLICATIONS &amp; INFORMATION SERVICES</div>
  <div class="pn">27</div>
</section>

<!-- Row 10 -->
<section class="slide c1" style="top:2088px">
  <div class="title" style="top:12px;color:#222">BOOKS</div>
  <div class="abs" role="img" aria-label="Grid of book covers" style="left:50px;top:42px;width:284px;height:160px">
    <div class="cover" style="left:0;top:0;background:#2a5a8a"></div><div class="cover" style="left:48px;top:0;background:#8a5a2a"></div><div class="cover" style="left:96px;top:0;background:#d8d0c0"></div><div class="cover" style="left:144px;top:0;background:#e8e0d0"></div><div class="cover" style="left:192px;top:0;background:#e08a4a"></div><div class="cover" style="left:240px;top:0;background:#4a8ab8"></div>
    <div class="cover" style="left:0;top:56px;background:#c8a070"></div><div class="cover" style="left:48px;top:56px;background:#d89030"></div><div class="cover" style="left:96px;top:56px;background:#6a9ad0"></div><div class="cover" style="left:144px;top:56px;background:#e8d890"></div><div class="cover" style="left:192px;top:56px;background:#c0c8d8"></div><div class="cover" style="left:240px;top:56px;background:#9a7a4a"></div>
    <div class="cover" style="left:0;top:112px;background:#e0902a"></div><div class="cover" style="left:48px;top:112px;background:#5a2a6a"></div><div class="cover" style="left:96px;top:112px;background:#2ea44f"></div><div class="cover" style="left:144px;top:112px;background:#1f7a3e"></div><div class="cover" style="left:192px;top:112px;background:#a8a8a0"></div><div class="cover" style="left:240px;top:112px;background:#3a6a9a"></div>
  </div>
  <div class="foot">PUBLICATIONS &amp; INFORMATION SERVICES</div>
  <div class="mk"></div><div class="pn">28</div>
</section>

<section class="slide c2" style="top:2088px">
  <div class="photo" role="img" aria-label="Pale city skyline background" style="inset:0;background:linear-gradient(180deg,#f4efe4,#e6ddc8)"></div>
  <div class="title" style="top:12px;font-size:18px">REPORTS</div>
  <div class="abs" role="img" aria-label="Report covers" style="left:58px;top:44px;width:270px;height:160px">
    <div class="cover" style="left:0;top:0;width:54px;height:72px;background:#e88a2a"></div><div class="cover" style="left:72px;top:0;width:54px;height:72px;background:#3a8ad0"></div><div class="cover" style="left:144px;top:0;width:54px;height:72px;background:#d06a2a"></div><div class="cover" style="left:216px;top:0;width:54px;height:72px;background:#e0a030"></div>
    <div class="cover" style="left:0;top:84px;width:54px;height:72px;background:#1a2a4a"></div><div class="cover" style="left:72px;top:84px;width:54px;height:72px;background:#2a6a7a"></div><div class="cover" style="left:144px;top:84px;width:54px;height:72px;background:#3a4a6a"></div><div class="cover" style="left:216px;top:84px;width:54px;height:72px;background:#8a6a4a"></div>
  </div>
  <div class="foot">PUBLICATIONS &amp; INFORMATION SERVICES</div>
  <div class="mk"></div><div class="pn">29</div>
</section>

<section class="slide c3" style="top:2088px">
  <div class="title" style="top:14px;font-size:18px;color:#222">VOLMA JOURNALS</div>
  <div class="abs" style="left:0;top:78px;width:384px;height:84px;background:var(--gr)"></div>
  <div class="abs" role="img" aria-label="Three journal covers" style="left:44px;top:52px;width:296px;height:132px">
    <div class="cover" style="left:0;top:0;width:84px;height:126px;background:linear-gradient(180deg,#fff 0 14px,#5aa860 14px)"></div>
    <div class="cover" style="left:106px;top:0;width:84px;height:126px;background:linear-gradient(180deg,#fff 0 14px,#2ea44f 14px)"></div>
    <div class="cover" style="left:212px;top:0;width:84px;height:126px;background:linear-gradient(180deg,#fff 0 14px,#1f7a3e 14px)"></div>
  </div>
  <div class="foot">PUBLICATIONS &amp; INFORMATION SERVICES</div>
  <div class="mk"></div><div class="pn">30</div>
</section>

<!-- Row 11 -->
<section class="slide c2" style="top:2318px">
  <div class="abs" style="left:0;top:0;width:384px;height:44px;text-align:center;line-height:50px;font-size:20px;font-weight:500;color:var(--dk)">Get in touch via</div>
  <div class="photo" role="img" aria-label="Dark perspective hallway" style="left:0;top:48px;width:384px;height:156px;background:linear-gradient(120deg,#2a2a2a,#4a4a4a 50%,#222)"></div>
  <div class="abs" style="left:24px;top:108px;color:#fff;font-weight:700;font-size:22px">THANK YOU!</div>
  <div class="abs" style="left:206px;top:60px;font-size:6px;color:#fff;line-height:28px">
    <div><span class="dot"></span>+000 12 555 0100</div>
    <div><span class="dot"></span>info@volma.org</div>
    <div><span class="dot"></span>www.volma.org</div>
    <div><span class="dot"></span>+000 12 555 0199</div>
  </div>
  <div class="abs" style="left:8px;top:170px;font-size:5px;color:#fff">volma_acad &nbsp; volma</div>
  <div class="abs" style="left:8px;top:178px;display:flex;gap:5px">
    <span style="width:12px;height:12px;border-radius:50%;background:#3a9ae0"></span><span style="width:12px;height:12px;border-radius:50%;background:#3a5a9a"></span><span style="width:12px;height:12px;border-radius:50%;background:#2a7ab0"></span><span style="width:12px;height:12px;border-radius:50%;background:#d03a2a"></span>
  </div>
  <div class="mk"></div><div class="pn">31</div>
</section>

</body>
</html>
```